Web Design Project for Lark Meadow

We are a Honey Packing Company called Lark Meadow.
We need a new website.
We are open to many ideas.
We want to have headings like: Home/Products/About Us/Contact Us
We want an easy and uncomplicated website.
We need our logo attached to the center top or left top of the webpage.
We want to have a number of our products on the first page that increase in size once the cursor is placed on them.
We want to be able to add photos and products in the future as we expand.
Target Market(s)
Public
Food Distributors
Importers/Exporters
Industry/Entity Type
It Company
Look and feel
Each slider illustrates characteristics of the customer's brand and the style your logo design should communicate.

```html
<!DOCTYPE html>
<html lang="en">
<head>
<meta charset="utf-8">
<title>Lark Meadow – Products</title>
<link rel="stylesheet" href="https://fonts.googleapis.com/css2?family=Asap:wght@400;600;700&family=Arimo:wght@400;700&display=swap">
<style>
  :root {
    --page-yellow: #fdd01a;
    --corner-amber: #e5a80d;
    --ink: #222222;
    --muted: #7a7a7a;
    --nav-active: #252525;
    --nav-divider: #b5b5b5;
    --panel: #ffffff;
    --rule: #dcdcdc;
    --band: #e3e3e3;
    --button: #2466c4;
    --button-edge: #1a4f9e;
  }
  * { margin: 0; padding: 0; box-sizing: border-box; }
  html, body { width: 1200px; height: 730px; overflow: hidden; }
  body { background: var(--page-yellow); font-family: "Arimo", Arial, sans-serif; color: var(--ink); }
  .site { position: relative; width: 1000px; height: 730px; margin: 0 auto; }

  .brand { position: absolute; left: 0; top: 6px; font-family: "Asap", sans-serif; font-weight: 400; font-size: 33px; color: var(--ink); }
  .product-count { position: absolute; right: 2px; top: 35px; font-size: 12px; }

  .main-nav { position: absolute; top: 102px; left: 0; width: 1000px; height: 58px; background: var(--panel); display: flex; }
  .main-nav a { display: flex; align-items: center; justify-content: center; height: 58px; font-size: 13px; color: var(--ink); text-decoration: none; letter-spacing: .3px; position: relative; }
  .main-nav a.is-active { background: var(--nav-active); color: #fff; }
  .main-nav a.has-divider::after { content: ""; position: absolute; right: 0; top: 11px; height: 37px; border-right: 1px solid var(--nav-divider); }
  .nav-home { width: 114px; }
  .nav-products { width: 143px; }
  .nav-about { width: 141px; }
  .nav-contact { width: 158px; }

  .hero { position: absolute; top: 160px; left: 0; width: 1000px; height: 290px; }
  .hero-photo { position: absolute; left: 19px; top: 0; width: 961px; height: 290px;
    background: radial-gradient(ellipse at 45% 45%, #e9a53e 0%, #c77417 45%, #8a3d08 80%, #f4ede4 100%); }
  .hero-corner { position: absolute; width: 0; height: 0; }
  .corner-tl { left: 0; top: 0; border-top: 19px solid var(--corner-amber); border-right: 19px solid transparent; }
  .corner-tr { right: 0; top: 0; border-top: 19px solid var(--corner-amber); border-left: 19px solid transparent; }
  .corner-bl { left: 0; bottom: 0; border-bottom: 19px solid var(--corner-amber); border-right: 19px solid transparent; }
  .corner-br { right: 0; bottom: 0; border-bottom: 19px solid var(--corner-amber); border-left: 19px solid transparent; }

  .hero-band { position: absolute; top: 450px; left: 0; width: 1000px; height: 16px; background: var(--band); }

  .content { position: absolute; top: 466px; left: 0; width: 1000px; height: 300px; background: var(--panel); padding: 26px 33px 0 35px; }
  .section-title { font-family: "Asap", sans-serif; font-weight: 600; font-size: 22px; color: var(--ink); padding-bottom: 5px; border-bottom: 1px solid var(--rule); }
  .product-grid { display: grid; grid-template-columns: 471px 460px; row-gap: 25px; margin-top: 13px; }
  .product-card { display: flex; gap: 10px; margin-left: 2px; transition: transform .2s; }
  .product-card:hover { transform: scale(1.04); }
  .product-photo { width: 225px; height: 149px; flex: none; background: linear-gradient(180deg, #8d8d8d 0%, #b9b9b9 60%, #d8d8d8 100%); position: relative; }
  .product-photo::after { content: ""; position: absolute; left: 60px; top: 10px; width: 105px; height: 139px; border-radius: 14px 14px 6px 6px; background: linear-gradient(180deg, #f0a21a, #d46b0a); }
  .product-name { font-family: "Asap", sans-serif; font-weight: 600; font-size: 20px; color: var(--muted); line-height: 25px; margin-top: -1px; }
  .product-desc { font-size: 13px; color: var(--muted); margin-top: 3px; }
  .product-price { font-size: 13px; font-weight: 700; color: #666; margin-top: 10px; }
  .add-to-cart { display: inline-block; margin-top: 9px; padding: 4px 9px; font-size: 11px; font-weight: 700; color: #fff; background: var(--button); border: 1px solid var(--button-edge); border-radius: 4px; }
</style>
</head>
<body>
<div class="site">
  <header>
    <div class="brand">Lark Meadow</div>
    <div class="product-count">Number of Products &nbsp;:&nbsp; 6</div>
  </header>

  <nav class="main-nav">
    <a class="nav-home" href="#">HOME</a>
    <a class="nav-products is-active" href="#">PRODUCTS</a>
    <a class="nav-about has-divider" href="#">ABOUT US</a>
    <a class="nav-contact has-divider" href="#">CONTACT US</a>
  </nav>

  <section class="hero">
    <div class="hero-photo" role="img" aria-label="Close-up of a honey dipper resting in a glass jar of golden honey"></div>
    <span class="hero-corner corner-tl"></span>
    <span class="hero-corner corner-tr"></span>
    <span class="hero-corner corner-bl"></span>
    <span class="hero-corner corner-br"></span>
  </section>
  <div class="hero-band"></div>

  <main class="content">
    <h2 class="section-title">Our Quality Products</h2>
    <div class="product-grid">
      <article class="product-card">
        <div class="product-photo" role="img" aria-label="Plastic jar of pure honey, 500 g"></div>
        <div>
          <h3 class="product-name">Pure Honey 500 g. Jar</h3>
          <p class="product-desc">Pure Honey 500 g. Jar</p>
          <p class="product-price">$100.00</p>
          <span class="add-to-cart">Add to Cart</span>
        </div>
      </article>
      <article class="product-card">
        <div class="product-photo" role="img" aria-label="Tub of blue gum honey, 1 kg"></div>
        <div>
          <h3 class="product-name">Blue Gum 1 kg. Jar</h3>
          <p class="product-desc">Blue Gum 1 kg. Jar</p>
          <p class="product-price">$100.00</p>
          <span class="add-to-cart">Add to Cart</span>
        </div>
      </article>
      <article class="product-card">
        <div class="product-photo" role="img" aria-label="Squeeze bottle of pure honey, 360 g"></div>
        <div>
          <h3 class="product-name">Pure Honey 360 g.<br>Squeeze</h3>
          <p class="product-desc">Pure Honey 360 g. Squeeze</p>
          <p class="product-price">$100.00</p>
          <span class="add-to-cart">Add to Cart</span>
        </div>
      </article>
      <article class="product-card">
        <div class="product-photo" role="img" aria-label="Tub of pure honey, 1 kg"></div>
        <div>
          <h3 class="product-name">Pure Honey 1 kg.</h3>
          <p class="product-desc">Pure Honey 1 kg.</p>
          <p class="product-price">$100.00</p>
          <span class="add-to-cart">Add to Cart</span>
        </div>
      </article>
    </div>
  </main>
</div>
</body>
</html>
```